Card for invoking rights with police

Our criminal defense law firm is seeking proposals for a design for our card intended for clients to carry with them in their car. Upon being pulled over, they would hand this card to the officer.
Text for the back of the card:
"For Law Enforcement:"
"I will comply with lawful orders but respectfully decline any test or other requests without my attorney. I wish to remain silent, do not consent to searches, and request to speak with my attorney now.
The back of the card should prominently feature the text and the firm logo should be secondary.
Front
Must prominently feature contact info: 503-555-0182. Do not include attorney name, email, phone from the example file. This is intended to be generic for the firm and not tied to an individual lawyer.
Included for design reference: current business card, firm logo.
We intend to use trenvo.com to produce the cards.
Updates
The back of the card should prominently display the text regarding invocation of rights. Please title it "For Law Enforcement".
Target Market(s)
People who have been stopped by police
Contact Information for Business Card
see project description
Look and feel

```html
<!DOCTYPE html>
<html lang="en">
<head>
<meta charset="utf-8">
<title>Halvern Law Firm – Rights Card</title>
<link rel="stylesheet" href="https://fonts.googleapis.com/css2?family=Open+Sans:wght@400;600;700&display=swap">
<style>
  :root {
    --navy: #0b2d4d;
    --paper: #ffffff;
    --backdrop: #e4e4e4;
    --ink: #3a3a3a;
    --on-navy: #ffffff;
  }
  * { box-sizing: border-box; margin: 0; padding: 0; }
  html, body {
    width: 1200px; height: 1200px; overflow: hidden;
    background: var(--backdrop);
    font-family: "Open Sans", Arial, sans-serif;
  }
  .card {
    position: absolute; left: 160px; width: 880px; height: 508px; overflow: hidden;
  }
  .card--front { top: 55px; background: var(--paper); color: var(--ink); }
  .card--back { top: 637px; background: var(--navy); color: var(--on-navy); }

  .brand {
    position: absolute; display: flex; align-items: center; gap: 18px;
    font-weight: 600; letter-spacing: 4px; text-transform: uppercase; white-space: nowrap;
  }
  .brand__square { width: 64px; height: 64px; flex: none; }
  .card--front .brand { left: 424px; top: 120px; color: var(--navy); font-size: 30px; }
  .card--front .brand__square { background: var(--navy); }
  .card--back .brand {
    left: 50%; transform: translateX(-50%); top: 52px;
    color: var(--on-navy); font-size: 24px; gap: 14px; letter-spacing: 3px;
  }
  .card--back .brand__square { background: var(--on-navy); width: 46px; height: 46px; }

  .phone-band {
    position: absolute; left: 461px; top: 251px; width: 419px; height: 86px;
    background: var(--navy); color: var(--on-navy);
    display: flex; align-items: center; justify-content: flex-end;
    padding-right: 66px;
    font-size: 30px; font-weight: 700; letter-spacing: 1px;
  }

  .contact-list {
    position: absolute; left: 46px; top: 290px; list-style: none;
    font-size: 19px; line-height: 34.5px;
  }
  .contact-list li { display: flex; align-items: center; gap: 10px; }
  .contact-list svg { width: 18px; height: 18px; fill: var(--navy); flex: none; }

  .address {
    position: absolute; right: 66px; top: 373px; text-align: right;
    font-size: 19px; line-height: 27px; font-style: normal;
  }

  .rights {
    position: absolute; left: 40px; right: 40px; top: 142px; text-align: center;
  }
  .rights__title { font-size: 32px; font-weight: 700; line-height: 42px; margin-bottom: 12px; }
  .rights__text { font-size: 22px; line-height: 33px; }

  .web {
    position: absolute; left: 0; right: 0; top: 432px; text-align: center;
    font-size: 19px; letter-spacing: 6px;
  }
</style>
</head>
<body>
  <section class="card card--front" aria-label="Card front">
    <div class="brand"><span class="brand__square"></span>Halvern Law Firm</div>

    <div class="phone-band">503-555-0182</div>

    <ul class="contact-list">
      <li><svg viewBox="0 0 20 20"><path d="M2 7c0-3 3-4 8-4s8 1 8 4v1h-4V6H6v2H2z M4 10h12l2 7H2z M10 11a2.5 2.5 0 1 0 0 5a2.5 2.5 0 1 0 0-5z"/></svg>503-555-0182</li>
      <li><svg viewBox="0 0 20 20"><path d="M6 1h8a1.5 1.5 0 0 1 1.5 1.5v15A1.5 1.5 0 0 1 14 19H6a1.5 1.5 0 0 1-1.5-1.5v-15A1.5 1.5 0 0 1 6 1zm0.5 2.5v11h7v-11zM10 15.5a1 1 0 1 0 0 2a1 1 0 1 0 0-2z"/></svg>503-555-0182</li>
      <li><svg viewBox="0 0 20 20"><path d="M5 2h10v5H5z M1 8h18v7H1z M5 13h10v5H5z"/></svg>503-555-0183</li>
      <li><svg viewBox="0 0 20 20"><path d="M1 4h18v1.5l-9 6l-9-6z M1 7.5l9 6l9-6V16H1z"/></svg>info@halvernlaw.com</li>
      <li><svg viewBox="0 0 20 20"><path d="M10 1a9 9 0 1 0 0 18a9 9 0 1 0 0-18zm-1 3l-2 3l2 2l-1 3l2 3l-1 2a7 7 0 0 1-5-12zm3 0a7 7 0 0 1 4.5 10l-2-1l-1-3l2-2z"/></svg>www.halvernlaw.com</li>
    </ul>

    <address class="address">
      2150 Cedar Crest Ave NE<br>
      Suite 410<br>
      Riverton, WA 98120
    </address>
  </section>

  <section class="card card--back" aria-label="Card back">
    <div class="brand"><span class="brand__square"></span>Halvern Law Firm</div>

    <div class="rights">
      <h2 class="rights__title">For Law Enforcement:</h2>
      <p class="rights__text">
        I will comply with lawful orders but respectfully decline<br>
        any test or other requests without my attorney.<br>
        I wish to remain silent, do not consent to searches,<br>
        and request to speak with my attorney now.
      </p>
    </div>

    <div class="web">www.halvernlaw.com</div>
  </section>
</body>
</html>
```